Wilderness Doc & TV personality personal page

I’m a wilderness and EMS emergency physician with particular sub specialties and a TV show. I need a website to highlight my interviews, teachings, etc... I did buy a number of domains for now.
Topics and things I need: CV (or version) me in the media, picture gallery, actually I sort of really like what dr owen parkes, my colleague has setup plus I have tv show and stuff like that. ridgeline tracker dot com

Target Market(s)

EMS, education, commercial products...

Industry/Entity Type

Medical And Science

Coding

Coded - Design and coding required

Number of Pages Required

1 page

Font styles to use
Sans Serif

Colors
f37122
9bcb3c
0556a4
a54499

Requirements
Must have
• Links and photos to news articles and things that mention me that I can add in.
Nice to have
• Maybe some snapshots of lecture reviews or patient thank you notes. Accolades so to speak
• I really appreciate how sharp it is. I would love to see Headings that resemble my friend's at ridgeline tracker dot com. Home, experience, consulting, lectures, affiliates, contact... those are main subjects... I think media also and that will have the TV show stuff and articles written about me...then maybe at the bottom of main page also have splits for training, research, television, and maybe exploration
Should not have
• The medical symbol with two snakes... that means quack doctor

```html
<!DOCTYPE html>
<html lang="en">
<head>
<meta charset="utf-8">
<title>Sam Lorne – Wilderness and EMS Emergency Physician</title>
<link rel="stylesheet" href="https://fonts.googleapis.com/css2?family=Fira+Sans:wght@400;500;600;700&family=Roboto:wght@400;500;700&display=swap">
<style>
:root{
  --navy:#0d4a82;
  --navy-deep:#0a3566;
  --card:#0b2f57;
  --green:#22a33a;
  --green-bright:#1fae3f;
  --ink:#1b1b1b;
  --text:#666;
  --light:#f1f1f1;
  --white:#fff;
}
*{box-sizing:border-box;margin:0;padding:0}
html,body{width:1200px;height:4438px;overflow:hidden}
body{position:relative;font-family:"Roboto",Arial,sans-serif;color:var(--ink);background:var(--white)}
.abs{position:absolute}
h1,h2,h3,h4{font-family:"Fira Sans",Arial,sans-serif}

/* header */
.site-header{left:0;top:0;width:1200px;height:85px;background:var(--navy);z-index:5}
.brand{left:141px;top:14px;font:400 42px/1 "Fira Sans",sans-serif;color:var(--white)}
.main-nav{left:389px;top:31px;display:flex;gap:25px}
.main-nav a{color:var(--white);text-decoration:none;font:600 16px/1 "Fira Sans",sans-serif;letter-spacing:.3px}
.nav-pointer{left:402px;top:0}
.social{left:908px;top:25px;display:flex;gap:6px}
.social span{width:30px;height:30px;border:2px solid var(--white);border-radius:50%}

/* hero */
.hero{left:0;top:85px;width:1200px;height:640px;background:#f4efea;overflow:hidden}
.hero-photo{left:420px;top:0;width:780px;height:640px;background:linear-gradient(180deg,#cfdbe3 0%,#8fae84 45%,#3f7a3c 100%);-webkit-mask-image:linear-gradient(90deg,transparent 0%,#000 35%);mask-image:linear-gradient(90deg,transparent 0%,#000 35%)}
.hero-name{left:140px;top:275px;font:600 64px/1 "Fira Sans",sans-serif;color:#1c1c1c}
.hero-role{left:143px;top:356px;font:400 32px/41px "Fira Sans",sans-serif;color:#2a2a2a}
.btn{display:flex;align-items:center;justify-content:center;border-radius:22px;font:700 15px/1 "Fira Sans",sans-serif;letter-spacing:.4px}
.btn-solid{left:145px;top:467px;width:164px;height:43px;background:var(--navy);color:var(--white)}
.btn-outline{left:327px;top:467px;width:178px;height:43px;border:3px solid var(--navy);color:var(--navy);gap:10px}
.slide-arrow{top:256px;width:40px;height:40px;border-radius:50%;background:#1d1d1d;display:flex;align-items:center;justify-content:center}
.hero-wave{left:0;top:555px}

/* about */
.about-frame{left:133px;top:791px;width:236px;height:12px;background:var(--navy)}
.about-frame-side{left:133px;top:791px;width:10px;height:250px;background:var(--navy)}
.about-photo{left:143px;top:799px;width:408px;height:471px;background:linear-gradient(135deg,#2f8c4e 0%,#1b6d7e 45%,#173b73 100%)}
.about-kicker{left:583px;top:808px;font:500 28px/1 "Fira Sans",sans-serif;color:#222}
.about-title{left:583px;top:842px;font:600 48px/1.1 "Fira Sans",sans-serif;color:#1b1b1b}
.about-text{left:583px;top:906px;width:472px;font:400 15px/24px "Roboto",sans-serif;color:var(--text)}
.btn-about{left:583px;top:1097px;width:146px;height:41px;background:var(--navy);color:var(--white)}
.info-strip{left:400px;top:1178px;width:657px;height:95px;background:var(--light);display:flex}
.info-item{display:flex;align-items:center;gap:12px;padding-left:24px;border-right:1px solid #dadada;font:400 13.5px/19px "Roboto",sans-serif;color:#555}
.info-item:nth-child(1){width:222px}
.info-item:nth-child(2){width:200px}
.info-item:nth-child(3){width:235px;border-right:none;padding-left:26px}

/* services */
.services-bg{left:0;top:1330px}
.svc{display:flex;flex-direction:column;align-items:center;text-align:center;color:var(--white);border-radius:50%}
.svc-side{width:282px;height:282px;background:var(--green);padding:38px 34px 0}
.svc-side h3{font:600 18px/1 "Fira Sans",sans-serif;margin:14px 0 12px;letter-spacing:.3px}
.svc-side p{font:400 14px/24px "Roboto",sans-serif}
.svc-main-ring{left:410px;top:1355px;width:380px;height:380px;border-radius:50%;background:#f4f4f4}
.svc-main{left:426px;top:1371px;width:348px;height:348px;background:var(--navy);padding:34px 36px 0}
.svc-main h3{font:600 22px/1 "Fira Sans",sans-serif;margin:12px 0 14px;letter-spacing:.4px}
.svc-main p{font:400 14px/25.5px "Roboto",sans-serif}
.svc-main a{display:block;margin-top:10px;color:var(--white);font:700 12.5px/1 "Roboto",sans-serif}

/* section headings */
.sec-title{width:1200px;left:0;text-align:center;font:600 37px/1 "Fira Sans",sans-serif}
.sec-rule{left:532px}

/* tv show */
.tv-card{top:1928px;width:295px;height:386px;background:var(--card);text-align:center;color:var(--white)}
.tv-thumb{position:absolute;left:6px;top:6px;width:283px;height:186px;display:flex;align-items:center;justify-content:center}
.tv-card h4{position:absolute;top:218px;width:100%;font:500 20px/1 "Fira Sans",sans-serif}
.tv-card p{position:absolute;top:257px;left:27px;width:241px;font:400 14px/22px "Roboto",sans-serif;color:#dfe6ee}
.tv-card .more{position:absolute;top:344px;width:100%;font:700 11.5px/1 "Roboto",sans-serif;letter-spacing:.3px}

/* gallery */
.gal{background:#888}
.gal-caption{left:30px;top:170px;color:var(--white);border-left:2px solid var(--white);padding-left:24px}
.gal-caption h4{font:500 20px/1 "Fira Sans",sans-serif;letter-spacing:.3px}
.gal-caption p{margin-top:12px;font:500 14px/1 "Roboto",sans-serif}

/* appointment */
.appt{left:0;top:3285px;width:1200px;height:710px;background:radial-gradient(ellipse at 50% 60%,#232323 0%,#111 70%)}
.field{left:221px;width:366px;height:40px;border:1px solid #bdbdbd;color:#eee;font:400 12px/1 "Roboto",sans-serif;padding:13px 13px}
.field-msg{left:606px;top:3577px;width:372px;height:194px}
.submit{left:525px;top:3804px;width:157px;height:43px;background:var(--green);color:var(--white);border-radius:2px;font:700 18px/43px "Fira Sans",sans-serif;text-align:center;letter-spacing:.5px}
.skyline{left:0;top:3943px;width:1200px;height:52px;background:linear-gradient(180deg,#2b2b2b,#0f0f0f)}

/* footer */
.site-footer{left:0;top:3995px;width:1200px;height:443px;background:var(--white)}
.foot-h{font:500 18px/1 "Fira Sans",sans-serif;color:#1b1b1b}
.foot-p{font:400 13.5px/20px "Roboto",sans-serif;color:#444}
.foot-row{display:flex;gap:16px;align-items:flex-start}
.foot-ico{width:28px;height:28px;border:1.5px solid #333;border-radius:4px;display:flex;align-items:center;justify-content:center;flex-shrink:0}
.foot-social{display:flex;gap:6px}
.foot-social span{width:34px;height:34px;border:1.5px solid #333;border-radius:50%}
.email-box{width:272px;height:40px;border:1px solid #cfcfcf;border-radius:20px;padding:13px 16px;font:400 10px/1 "Roboto",sans-serif;color:#777}
.btn-signup{width:114px;height:34px;background:var(--green-bright);color:var(--white);border-radius:17px;font:700 15px/34px "Fira Sans",sans-serif;text-align:center}
.quick a{display:block;color:#333;text-decoration:none;font:400 13.5px/26px "Roboto",sans-serif}
.copyright{left:0;top:4358px;width:1200px;border-top:1px solid #e2e2e2;padding-top:30px;text-align:center;font:400 13.5px/1 "Roboto",sans-serif;color:#444}
</style>
</head>
<body>

<header class="site-header abs">
  <div class="brand abs">Sam Lorne</div>
  <svg class="nav-pointer abs" width="26" height="12" viewBox="0 0 26 12"><path d="M0 0 H26 L13 12 Z" fill="#fff"/></svg>
  <nav class="main-nav abs">
    <a href="#">HOME</a><a href="#">CV</a><a href="#">TV SHOW</a><a href="#">GALLERY</a><a href="#">MEDIA</a><a href="#">CONTACT</a>
  </nav>
  <div class="social abs" aria-label="Social profiles"><span></span><span></span><span></span><span></span></div>
</header>

<section class="hero abs">
  <div class="hero-photo abs" role="img" aria-label="Portrait of the physician in blue scrubs with a stethoscope, arms crossed, by the waterfront"></div>
  <h1 class="hero-name abs">Sam Lorne</h1>
  <p class="hero-role abs">Wilderness and EMS<br>Emergency physician</p>
  <div class="btn btn-solid abs">GET A QUOTE</div>
  <div class="btn btn-outline abs">WATCH VIDEO
    <svg width="26" height="26" viewBox="0 0 26 26"><circle cx="13" cy="13" r="11" fill="none" stroke="#0d4a82" stroke-width="2.5"/><path d="M10 8 L18 13 L10 18 Z" fill="#0d4a82"/></svg>
  </div>
  <div class="slide-arrow abs" style="left:73px"><svg width="14" height="14" viewBox="0 0 14 14"><path d="M9 2 L4 7 L9 12" fill="none" stroke="#fff" stroke-width="1.8"/></svg></div>
  <div class="slide-arrow abs" style="left:1085px"><svg width="14" height="14" viewBox="0 0 14 14"><path d="M5 2 L10 7 L5 12" fill="none" stroke="#fff" stroke-width="1.8"/></svg></div>
  <svg class="hero-wave abs" width="1200" height="85" viewBox="0 0 1200 85">
    <path d="M0 38 C300 42 700 40 1200 0 V85 H0 Z" fill="#0d4a82"/>
    <path d="M0 52 C320 58 740 60 1200 26 V85 H0 Z" fill="#fff"/>
  </svg>
</section>

<section class="about">
  <div class="about-frame abs"></div>
  <div class="about-frame-side abs"></div>
  <div class="about-photo abs" role="img" aria-label="Smiling portrait of the physician in front of a green and teal painted wall"></div>
  <h3 class="about-kicker abs">Cv me in media</h3>
  <h2 class="about-title abs">About Sam Lorne</h2>
  <p class="about-text abs">Sed ut perspiciatis unde omnis iste natus error sit voluptatem accsantium doloremque laudantium, totam rem aperiam, eaque ipsa quae ab illo inventore veritatis et quasi architecto beatae vitae dicta sunt explicabo. Nemo enim ipsam voluptatem quia voluptas sit aatur aut odit aut fugit, sed quia consequuntur magni dolores eos qui ratine voluptatem sequi nesciunt. Neque porro quisquam est, qui dolorem ipsum quia dolor sit amet, consectetur</p>
  <div class="btn btn-about abs">READ MORE</div>
  <div class="info-strip abs">
    <div class="info-item">
      <svg width="16" height="22" viewBox="0 0 16 22"><path d="M8 1 C4 1 1 4 1 8 C1 13 8 21 8 21 C8 21 15 13 15 8 C15 4 12 1 8 1 Z" fill="none" stroke="#0d4a82" stroke-width="1.6"/><circle cx="8" cy="8" r="2.5" fill="none" stroke="#0d4a82" stroke-width="1.6"/></svg>
      <span>88 Cedar Hill Rd,<br>Ashgrove, 4060</span>
    </div>
    <div class="info-item">
      <svg width="18" height="18" viewBox="0 0 18 18"><path d="M3 1 L7 5 L5 7 C6 10 8 12 11 13 L13 11 L17 15 L14 17 C7 16 2 11 1 4 Z" fill="none" stroke="#0d4a82" stroke-width="1.5"/></svg>
      <span>Phone:<br>(555) 0142 7788</span>
    </div>
    <div class="info-item">
      <svg width="20" height="14" viewBox="0 0 20 14"><rect x="1" y="1" width="18" height="12" fill="none" stroke="#0d4a82" stroke-width="1.5"/><path d="M1 1 L10 8 L19 1" fill="none" stroke="#0d4a82" stroke-width="1.5"/></svg>
      <span>E-mail:<br>hello@samlorne.example</span>
    </div>
  </div>
</section>

<svg class="services-bg abs" width="1200" height="1080" viewBox="0 0 1200 1080">
  <path d="M0 220 L430 190 L430 250 L0 270 Z" fill="#cfcfcf"/>
  <path d="M0 270 L430 250 L430 300 L0 320 Z" fill="#e6e6e6"/>
  <path d="M0 320 L1200 210 V1078 H0 Z" fill="#0d4a8a"/>
</svg>

<div class="svc svc-side abs" style="left:141px;top:1405px">
  <svg width="66" height="60" viewBox="0 0 66 60" fill="none" stroke="#fff" stroke-width="2"><rect x="20" y="4" width="40" height="28"/><circle cx="12" cy="22" r="9"/><path d="M3 22 H21 M12 13 V31"/><path d="M4 56 V46 Q12 38 20 46 V56 M20 46 L36 40"/><rect x="30" y="42" width="28" height="14"/></svg>
  <h3>TV SHOW</h3>
  <p>Lorem ipsum dolor sit amet, cosectetur adipiscing elit, sed do eiusmod tempor incididunt ut labore et dolore magna</p>
</div>
<div class="svc-main-ring abs"></div>
<div class="svc svc-main abs">
  <svg width="84" height="74" viewBox="0 0 84 74" fill="none" stroke="#fff" stroke-width="2.4"><path d="M38 8 H76 Q80 8 80 12 V36 Q80 40 76 40 H72 V50 L62 40 H50"/><path d="M8 24 H50 Q54 24 54 28 V54 Q54 58 50 58 H26 L14 68 V58 H8 Q4 58 4 54 V28 Q4 24 8 24 Z"/><path d="M14 36 H44 M14 46 H38"/></svg>
  <h3>INTERVIEWS</h3>
  <p>Lorem ipsum dolor sit amet, consectetur adipiscing elit, sed do eiusmod tempor incididunt ut labore et dolore magna aliqua. Ut enim ad minim veniam, quis nostrud exercitation ullamco</p>
  <a href="#"><u>READ MORE &gt;</u></a>
</div>
<div class="svc svc-side abs" style="left:773px;top:1405px">
  <svg width="66" height="62" viewBox="0 0 66 62" fill="none" stroke="#fff" stroke-width="2"><rect x="18" y="2" width="44" height="26"/><circle cx="12" cy="20" r="5"/><path d="M6 46 V32 H18 V46 M18 30 L30 18"/><circle cx="28" cy="42" r="4"/><circle cx="42" cy="42" r="4"/><circle cx="56" cy="42" r="4"/><path d="M22 60 V52 H34 V60 M36 60 V52 H48 V60 M50 60 V52 H62 V60"/></svg>
  <h3>TEACHINGS</h3>
  <p>Lorem ipsum dolor sit amet, cosectetur adipiscing elit, sed do eiusmod tempor incididunt ut labore et dolore magna</p>
</div>

<h2 class="sec-title abs" style="top:1805px;color:#fff">TV Show</h2>
<svg class="sec-rule abs" style="top:1866px" width="136" height="16" viewBox="0 0 136 16"><path d="M0 6 H52 M0 10 H52 M84 6 H136 M84 10 H136" stroke="#fff" stroke-width="1.4"/><circle cx="68" cy="8" r="6" fill="#fff"/><path d="M68 5 V11 M65 8 H71" stroke="#0d4a8c" stroke-width="1.6"/></svg>

<article class="tv-card abs" style="left:143px">
  <div class="tv-thumb" role="img" aria-label="Video still of the physician speaking on a stage with green lighting" style="background:linear-gradient(135deg,#1e6a3a,#3b2a2a 60%,#6b2b33)">
    <svg width="40" height="40" viewBox="0 0 40 40"><circle cx="20" cy="20" r="17" fill="none" stroke="#fff" stroke-width="3"/><path d="M16 12 L28 20 L16 28 Z" fill="#fff"/></svg>
  </div>
  <h4>Quis autem vel eum</h4>
  <p>Lorem ipsum dolor sit amet, nsectetur adipiscing elit, sed do eiusmod tempor incididunt ut labore</p>
  <div class="more">LEARN MORE ⊙</div>
</article>
<article class="tv-card abs" style="left:453px">
  <div class="tv-thumb" role="img" aria-label="Video still of a panel discussion at a long table" style="background:linear-gradient(135deg,#7a5a3c,#3b3b32 55%,#2c4a38)">
    <svg width="40" height="40" viewBox="0 0 40 40"><circle cx="20" cy="20" r="17" fill="none" stroke="#fff" stroke-width="3"/><path d="M16 12 L28 20 L16 28 Z" fill="#fff"/></svg>
  </div>
  <h4>Quis autem vel eum</h4>
  <p>Lorem ipsum dolor sit amet, nsectetur adipiscing elit, sed do eiusmod tempor incididunt ut labore</p>
  <div class="more">LEARN MORE ⊙</div>
</article>
<article class="tv-card abs" style="left:761px">
  <div class="tv-thumb" role="img" aria-label="Video still of a presenter in a venue beside a chalkboard menu" style="background:linear-gradient(135deg,#5a2622,#2a2020 50%,#8a7a70)">
    <svg width="40" height="40" viewBox="0 0 40 40"><circle cx="20" cy="20" r="17" fill="none" stroke="#fff" stroke-width="3"/><path d="M16 12 L28 20 L16 28 Z" fill="#fff"/></svg>
  </div>
  <h4>Quis autem vel eum</h4>
  <p>Lorem ipsum dolor sit amet, nsectetur adipiscing elit, sed do eiusmod tempor incididunt ut labore</p>
  <div class="more">LEARN MORE ⊙</div>
</article>

<h2 class="sec-title abs" style="top:2482px;color:#1b1b1b">Our Gallery</h2>
<svg class="sec-rule abs" style="top:2547px" width="136" height="16" viewBox="0 0 136 16"><path d="M0 6 H52 M0 10 H52 M84 6 H136 M84 10 H136" stroke="#0d4a82" stroke-width="1.4"/><circle cx="68" cy="8" r="6" fill="#0d4a82"/><path d="M68 5 V11 M65 8 H71" stroke="#fff" stroke-width="1.6"/></svg>

<div class="gal abs" role="img" aria-label="Physician in dress uniform and sunglasses in front of an ambulance" style="left:143px;top:2607px;width:300px;height:579px;background:linear-gradient(180deg,#b8b23a 0%,#8a8a6a 35%,#e8e8ec 70%,#d6d6dc 100%)"></div>
<div class="gal abs" role="img" aria-label="Field training scene with green overlay" style="left:453px;top:2607px;width:298px;height:284px;background:linear-gradient(135deg,#3fae55,#2a9a48)">
  <div class="gal-caption abs"><h4>SED UT PERSPICIATIS</h4><p>Nemo enim ipsam</p></div>
</div>
<div class="gal abs" role="img" aria-label="Close-up of gloved hands preparing an IV line" style="left:759px;top:2607px;width:297px;height:284px;background:linear-gradient(135deg,#c9b9a0,#6a5a4a 55%,#2e2e2e)"></div>
<div class="gal abs" role="img" aria-label="Tactical medic in helmet and black vest speaking on a radio" style="left:453px;top:2902px;width:241px;height:284px;background:linear-gradient(180deg,#6d7a6a,#2a2a2a 60%,#1a1a1a)"></div>
<div class="gal abs" role="img" aria-label="Gold medical director badge on dark fabric" style="left:703px;top:2902px;width:353px;height:284px;background:radial-gradient(circle at 55% 50%,#c9a23a 0%,#7a5a1a 40%,#2a1c10 80%)"></div>

<section class="appt abs">
  <svg class="abs" style="left:0;top:0" width="1200" height="120" viewBox="0 0 1200 120"><path d="M0 0 H1200 V20 L0 0 Z" fill="#fff"/><path d="M760 40 L1200 18 V64 L760 60 Z" fill="#a9a9a9"/><path d="M560 60 L1200 64 V116 Z" fill="#e2e2e2"/></svg>
</section>
<h2 class="sec-title abs" style="top:3443px;color:#fff">Make an Appointment</h2>
<svg class="sec-rule abs" style="top:3508px" width="136" height="16" viewBox="0 0 136 16"><path d="M0 6 H52 M0 10 H52 M84 6 H136 M84 10 H136" stroke="#fff" stroke-width="1.4"/><circle cx="68" cy="8" r="6" fill="#fff"/><path d="M68 5 V11 M65 8 H71" stroke="#111" stroke-width="1.6"/></svg>
<div class="field abs" style="top:3577px">Name</div>
<div class="field abs" style="top:3628px">Email</div>
<div class="field abs" style="top:3680px">Phone</div>
<div class="field abs" style="top:3731px">Subject</div>
<div class="field field-msg abs">Message</div>
<div class="submit abs">SUBMIT</div>
<div class="skyline abs" role="img" aria-label="Decorative city skyline silhouette"></div>

<footer class="site-footer abs">
  <div class="abs" style="left:120px;top:87px;width:210px">
    <h4 class="foot-h">CV me</h4>
    <p class="foot-p" style="margin-top:16px">Nemo enim ipsam voluptatem quia voluptas sit aspernatur aut odit aut fugit, sed quia Nemo enim ipsam voluptatem quia voluptas sit aspernatur aut odit aut fugit, sed quia</p>
    <div class="foot-social" style="margin-top:14px"><span></span><span></span><span></span><span></span></div>
  </div>
  <div class="abs" style="left:385px;top:82px;width:250px">
    <h4 class="foot-h">Contact Us</h4>
    <div class="foot-row" style="margin-top:18px"><div class="foot-ico"><svg width="12" height="16" viewBox="0 0 12 16"><path d="M6 1 C3 1 1 3 1 6 C1 10 6 15 6 15 C6 15 11 10 11 6 C11 3 9 1 6 1 Z" fill="none" stroke="#333" stroke-width="1.4"/></svg></div><p class="foot-p">Sam Lorne<br>270 Harbor Ave, 9th floor<br>Portsmouth, NH 03801</p></div>
    <div class="foot-row" style="margin-top:14px"><div class="foot-ico"><svg width="14" height="14" viewBox="0 0 18 18"><path d="M3 1 L7 5 L5 7 C6 10 8 12 11 13 L13 11 L17 15 L14 17 C7 16 2 11 1 4 Z" fill="none" stroke="#333" stroke-width="1.6"/></svg></div><p class="foot-p">Call us today:<br>(555) 0199-2045</p></div>
    <div class="foot-row" style="margin-top:14px"><div class="foot-ico"><svg width="16" height="11" viewBox="0 0 20 14"><rect x="1" y="1" width="18" height="12" fill="none" stroke="#333" stroke-width="1.6"/><path d="M1 1 L10 8 L19 1" fill="none" stroke="#333" stroke-width="1.6"/></svg></div><p class="foot-p">Email :<br>contact@samlorne.example</p></div>
  </div>
  <div class="abs" style="left:667px;top:82px;width:280px">
    <h4 class="foot-h">Sign up for newsletter</h4>
    <p class="foot-p" style="margin-top:18px">Excepteur sint occaecat cupidatat non proident, sunt in culpa qui officia deserunt</p>
    <div class="email-box" style="margin-top:10px">Enter email</div>
    <div class="btn-signup" style="margin-top:14px">SIGN UP</div>
  </div>
  <div class="abs quick" style="left:990px;top:82px">
    <h4 class="foot-h" style="margin-bottom:12px">Quick Links</h4>
    <a href="#">Home</a><a href="#">CV</a><a href="#">Tv Show</a><a href="#">Gallery</a><a href="#">Media</a><a href="#">Contact</a>
  </div>
</footer>
<div class="copyright abs">© Copyright 2019 Sam Lorne. All Rights Reserved.</div>

</body>
</html>
```